Creative Law Firm Business Card

attached are photos of myself and our office as well as language that I would like to see on the card, likely on the back, although I leave that to the designer. I have also attached copies of both sides of a marketing card that we produced just for ideas. I would like to find a tactful way to get my photo in along with the office. I attached copies of our logo, both normal and inverted.

I listed my name as Tom Hollis to be casual, however, it should probably read Thomas J Hollis

• attached file #8 has content.
• I would like my picture and the office photo on page 1
• The text, with the exception of the firm name "HOLLIS & DWYER" and the firm description underneath it "THE BUSINESS AND BANKRUPTCY LAWYERS", should be on the back. The layout and fonts are up to the designer

```html
<!DOCTYPE html>
<html lang="en">
<head>
<meta charset="utf-8">
<title>Hollis &amp; Dwyer Business Card</title>
<link rel="stylesheet" href="https://fonts.googleapis.com/css2?family=Cinzel:wght@400;600&family=Arimo:wght@400&display=swap">
<style>
  :root {
    --page-bg: #ececec;
    --slate: #4d5e79;
    --slate-text: #44546e;
    --card-white: #ffffff;
    --frame-dark: #2e2a18;
    --office-dark: #5e5530;
    --office-mid: #8f8453;
    --office-light: #c4b98a;
    --portrait-deep: #0f2c57;
    --portrait-light: #3f6fa8;
    --panel: rgba(20, 30, 48, 0.78);
    --ink-light: #ffffff;
  }
  * { box-sizing: border-box; margin: 0; padding: 0; }
  html, body { width: 1002px; height: 1200px; overflow: hidden; }
  body {
    background: var(--page-bg);
    font-family: "Arimo", Arial, sans-serif;
    position: relative;
  }
  .card {
    position: absolute;
    left: 71px;
    width: 860px;
    height: 498px;
    overflow: hidden;
    box-shadow: 0 2px 6px rgba(0,0,0,0.18);
  }

  /* Front */
  .card-front {
    top: 70px;
    border: 6px solid var(--frame-dark);
  }
  .office-photo {
    position: absolute; inset: 0;
    background:
      radial-gradient(ellipse at 75% 90%, var(--office-light) 0%, transparent 55%),
      linear-gradient(160deg, var(--office-mid) 0%, var(--office-dark) 45%, var(--office-mid) 75%, var(--office-light) 100%);
  }
  .portrait {
    position: absolute;
    left: 42px; top: 96px;
    width: 252px; height: 340px;
    border: 2px solid var(--frame-dark);
    background: radial-gradient(ellipse at 45% 35%, var(--portrait-light) 0%, var(--portrait-deep) 80%);
  }
  .info-panel {
    position: absolute;
    left: 296px; top: 118px;
    width: 520px; height: 310px;
    background: var(--panel);
    padding: 20px 22px;
    color: var(--ink-light);
  }
  .person-name {
    font-family: "Cinzel", Georgia, serif;
    font-weight: 600;
    font-size: 40px;
    letter-spacing: 1px;
    line-height: 1.1;
  }
  .person-title {
    font-size: 18px;
    margin-top: 8px;
    letter-spacing: 0.3px;
  }
  .person-experience { font-size: 18px; margin-top: 2px; }
  .contact { margin-top: 54px; font-size: 22px; line-height: 1.3; }

  /* Back */
  .card-back {
    top: 632px;
    background: var(--card-white);
  }
  .band {
    position: absolute; left: 0; right: 0;
    background: var(--slate);
    color: var(--ink-light);
    text-align: center;
  }
  .band-top { top: 0; height: 136px; display: flex; align-items: center; justify-content: center; gap: 14px; }
  .band-bottom { bottom: 0; height: 118px; padding-top: 30px; font-size: 20px; line-height: 1.6; }
  .firm-mark { width: 18px; height: 18px; background: var(--ink-light); }
  .firm-name {
    font-family: "Cinzel", Georgia, serif;
    font-weight: 400;
    font-size: 30px;
    letter-spacing: 1.5px;
  }
  .practice-areas {
    position: absolute; left: 0; right: 0; top: 164px;
    text-align: center;
    color: var(--slate-text);
    font-size: 21px;
    line-height: 1.3;
    list-style: none;
  }
  .tagline {
    position: absolute; left: 0; right: 0; top: 318px;
    text-align: center;
    color: var(--slate-text);
    font-size: 30px;
  }
</style>
</head>
<body>
  <section class="card card-front">
    <div class="office-photo" role="img" aria-label="Photo of the law office building with palm trees in warm sepia tones"></div>
    <div class="portrait" role="img" aria-label="Portrait photo of Thomas J Hollis in a dark suit"></div>
    <div class="info-panel">
      <h1 class="person-name">Thomas J Hollis</h1>
      <p class="person-title">STATE BAR CERTIFIED BANKRUPTCY SPECIALIST</p>
      <p class="person-experience">36 years experience - AV Grade</p>
      <p class="contact">714.555.0148<br>tom@hollisdwyer.com</p>
    </div>
  </section>

  <section class="card card-back">
    <header class="band band-top">
      <span class="firm-mark"></span>
      <span class="firm-name">HOLLIS &amp; DWYER</span>
    </header>
    <ul class="practice-areas">
      <li>COMMERCIAL LAW / LITIGATION</li>
      <li>REAL PROPERTY TRANSACTIONS / LITIGATION</li>
      <li>BANKRUPTCY AND REORGANISATIONS</li>
      <li>COLLECTIONS</li>
    </ul>
    <p class="tagline">We find an exit strategy before we act</p>
    <footer class="band band-bottom">
      2180 Canyon Ridge Rd Irvine, CA 92618<br>www.hollisdwyer.com
    </footer>
  </section>
</body>
</html>
```